Geothermal company needs a creative "POW" business card

Manufacturers tend to be boring. We are not! We are a Geothermal Heat Pump company that has over 30 yrs of experience and wants a new look and updated feel. Nothing old (yawn) so get your creative hats on and let's rock!

We want to use the great colors of lime green and navy blue. Our new logo is attached and we're ready to roll. Remember, we're a professional leader in the geothermal industry that needs to make an eye catching and memorable first glance.

```html
<!DOCTYPE html>
<html lang="en">
<head>
<meta charset="utf-8">
<title>Ironwood Heat – Business Card</title>
<link rel="stylesheet" href="https://fonts.googleapis.com/css2?family=Oswald:wght@500;600&display=swap">
<style>
  :root {
    --navy: #06244b;
    --lime: #78b800;
    --paper: #ffffff;
    --card-light: #f7f7f7;
    --card-dark: #cfcfcf;
    --bubble: rgba(255,255,255,0.55);
    --icon-light: #9fc9ef;
  }
  html, body {
    margin: 0;
    width: 1200px;
    height: 1000px;
    overflow: hidden;
    background: var(--paper);
  }
  .canvas { position: relative; width: 1200px; height: 1000px; }
  .card {
    position: absolute;
    left: 335px;
    width: 575px;
    height: 326px;
    display: block;
  }
  .card--front { top: 113px; }
  .card--back { top: 545px; }
  .type {
    font-family: "Oswald", "Arial Narrow", sans-serif;
    font-weight: 600;
  }
  .small-caps { font-variant: small-caps; }
  .brand-name { font-family: "Oswald", "Arial Narrow", sans-serif; font-weight: 500; font-size: 32px; fill: var(--lime); }
  .holder { font-size: 27px; fill: var(--paper); letter-spacing: 0.5px; }
  .email { font-size: 18px; fill: var(--lime); letter-spacing: 0.3px; }
  .web { font-size: 23px; fill: var(--navy); }
  .phone { font-size: 16px; fill: var(--navy); }
  .address { font-size: 20px; fill: var(--paper); }
  .bubble { fill: var(--bubble); }
  .fill-navy { fill: var(--navy); }
  .fill-lime { fill: var(--lime); }
</style>
</head>
<body>
<div class="canvas">

  <svg class="card card--front" viewBox="0 0 575 326" aria-label="Business card front">
    <defs>
      <radialGradient id="card-bg" cx="0.4" cy="0.45" r="0.75">
        <stop offset="0" stop-color="var(--card-light)"/>
        <stop offset="1" stop-color="var(--card-dark)"/>
      </radialGradient>
      <filter id="soft-shadow" x="-20%" y="-20%" width="140%" height="140%">
        <feDropShadow dx="3" dy="4" stdDeviation="3" flood-color="#000" flood-opacity="0.25"/>
      </filter>
      <clipPath id="front-clip"><rect width="575" height="326"/></clipPath>
    </defs>
    <rect width="575" height="326" fill="url(#card-bg)"/>
    <g clip-path="url(#front-clip)">
      <g class="bubbles">
        <circle class="bubble" cx="144" cy="249" r="47"/>
        <circle class="bubble" cx="36" cy="238" r="27"/>
        <circle class="bubble" cx="79" cy="297" r="21"/>
        <circle class="bubble" cx="79" cy="145" r="12"/>
        <circle class="bubble" cx="125" cy="188" r="17"/>
        <circle class="bubble" cx="206" cy="205" r="16"/>
        <circle class="bubble" cx="210" cy="260" r="12"/>
      </g>
      <circle class="fill-lime" cx="163" cy="164" r="23" filter="url(#soft-shadow)"/>
      <circle class="fill-navy" cx="252" cy="180" r="32" filter="url(#soft-shadow)"/>
      <circle class="fill-lime" cx="383" cy="181" r="73" filter="url(#soft-shadow)"/>
      <circle class="fill-navy" cx="515" cy="66" r="153" filter="url(#soft-shadow)"/>
    </g>
    <g class="brand">
      <circle class="fill-navy" cx="69" cy="73" r="44"/>
      <text class="brand-name" x="119" y="84">Ironwood Heat</text>
    </g>
    <text class="type small-caps holder" x="562" y="82" text-anchor="end">Ray Kestner</text>
    <text class="type small-caps holder" x="562" y="112" text-anchor="end">CEO</text>
  </svg>

  <svg class="card card--back" viewBox="0 0 575 326" aria-label="Business card back">
    <defs>
      <radialGradient id="card-bg-back" cx="0.55" cy="0.45" r="0.75">
        <stop offset="0" stop-color="var(--card-light)"/>
        <stop offset="1" stop-color="var(--card-dark)"/>
      </radialGradient>
      <clipPath id="back-clip"><rect width="575" height="326"/></clipPath>
    </defs>
    <rect width="575" height="326" fill="url(#card-bg-back)"/>
    <g class="bubbles">
      <circle class="bubble" cx="493" cy="250" r="40"/>
      <circle class="bubble" cx="403" cy="240" r="22"/>
      <circle class="bubble" cx="438" cy="162" r="10"/>
      <circle class="bubble" cx="477" cy="199" r="14"/>
      <circle class="bubble" cx="545" cy="212" r="13"/>
      <circle class="bubble" cx="548" cy="259" r="10"/>
      <circle class="bubble" cx="438" cy="289" r="17"/>
    </g>
    <g clip-path="url(#back-clip)">
      <circle class="address-band fill-navy" cx="120" cy="350" r="135"/>
    </g>

    <g class="icon icon--email">
      <circle class="fill-lime" cx="94" cy="77" r="27"/>
      <rect x="79" y="67" width="30" height="20" fill="var(--navy)"/>
      <path d="M79 67 L94 79 L109 67" fill="none" stroke="var(--paper)" stroke-width="1.5"/>
    </g>
    <text class="type email" x="129" y="84">RAYKESTNER@IRONWOODHEAT.COM</text>

    <g class="icon icon--web">
      <circle class="fill-navy" cx="94" cy="143" r="27"/>
      <g fill="none" stroke="var(--icon-light)" stroke-width="1.5">
        <circle cx="94" cy="143" r="10"/>
        <ellipse cx="94" cy="143" rx="4.5" ry="10"/>
        <line x1="84" y1="143" x2="104" y2="143"/>
        <line x1="86" y1="138" x2="102" y2="138"/>
        <line x1="86" y1="148" x2="102" y2="148"/>
      </g>
    </g>
    <text class="type web" x="125" y="153">WWW.IRONWOODHEAT.COM</text>

    <g class="icon icon--phone">
      <circle class="fill-navy" cx="94" cy="193" r="27"/>
      <path d="M86 181 c3 -2 5 0 6 3 l1 3 c0 2 -2 3 -3 4 c1 4 4 7 8 9 c1 -1 2 -3 4 -3 l3 1 c3 1 4 3 2 6 c-2 3 -6 4 -10 2 c-7 -4 -12 -10 -14 -17 c-1 -4 0 -6 3 -8z" fill="none" stroke="var(--icon-light)" stroke-width="1.6"/>
    </g>
    <text class="type small-caps phone" x="130" y="194">Phone: (555) 014-2200</text>
    <text class="type small-caps phone" x="130" y="211">Fax: (555) 014-2201</text>

    <text class="type small-caps address" x="38" y="272">48 N Larch Ave</text>
    <text class="type small-caps address" x="38" y="296">Pinecrest, MN 55900</text>
  </svg>

</div>
</body>
</html>
```